Keelridge Ventures Consulting firm

I need a business card that is succint for a Brisbane based business called Keelridge Ventures Consulting Pty Ltd.
We bridge the gaps between People, Process and Technology.

We are a specialist operational excellence firm, delivering strategic consulting and business advisory services in six core capabilities, across all industries and all business lines to improve performance, efficiency, profitability, automation and scalability, for clients across Australia &New Zealand.
Updates

Hi Designers, I have uploaded the logo in 3D .png format, to assist in card design.

Target Market(s)

Project Management professionals, IT professionals, corporate and government clients managing transitioning or transformation projects.

Contact Information for Business Card

Keelridge Ventures Consulting Pty Ltd

Daniel Ostrava
Principal Consultant

mobile: +61 452 160 389
email: daniel@keelridgeventuresconsulting.com.au
webpage: www.keelridgeventuresconsulting.com

professional services: strategic advisors,

Font styles to use
Sans Serif

Requirements
Must have
• Business name: Keelridge Ventures Consulting
logo: attached
Contact person: Daniel Ostrava
Title: Principal Consultant
contact details:
mobile +61 452 160
email: daniel@KeelridgeVenturesConsulting.com.au
website: KeelridgeVenturesConsulting.com

on back side with logo include: A.B.N. 71482903165

professional services offered: Business Analysis, Strategic Advisory
Nice to have
• QR code
Should not have
• contacts picture

```html
<!DOCTYPE html>
<html lang="en">
<head>
<meta charset="utf-8">
<title>Keelridge Ventures Consulting – Business Card</title>
<link href="https://fonts.googleapis.com/css2?family=Roboto:wght@400;500;700&family=Roboto+Condensed:wght@700&display=swap" rel="stylesheet">
<style>
  :root {
    --page-bg: #e6e6e6;
    --card-dark: #262626;
    --pattern-tone: #2e2e2e;
    --brand-red: #e8313a;
    --deep-maroon: #231a1b;
    --mid-red: #7a2428;
    --name-ink: #3a2526;
    --white: #ffffff;
    --icon-ring: #b8383e;
  }
  * { box-sizing: border-box; margin: 0; padding: 0; }
  html, body { width: 1200px; height: 1200px; overflow: hidden; }
  body {
    background: var(--page-bg);
    font-family: "Roboto", Arial, sans-serif;
    position: relative;
  }
  .card {
    position: absolute;
    left: 250px;
    width: 700px;
    height: 400px;
    border-radius: 22px;
    overflow: hidden;
  }
  /* Front face */
  .card-front { top: 178px; background: var(--card-dark); }
  .front-texture {
    position: absolute; inset: 0;
    background: linear-gradient(180deg, var(--pattern-tone), var(--card-dark));
  }
  .front-brand {
    position: absolute;
    left: 0; right: 0; top: 160px;
    text-align: center;
  }
  .brand-name {
    font-weight: 700;
    font-size: 44px;
    letter-spacing: 1px;
    color: var(--brand-red);
    line-height: 1;
    text-transform: uppercase;
  }
  .abn {
    margin-top: 14px;
    font-weight: 700;
    font-size: 11px;
    letter-spacing: 0.5px;
    color: var(--white);
  }
  /* Back face */
  .card-back {
    top: 622px;
    background: linear-gradient(90deg, var(--deep-maroon) 0%, var(--mid-red) 45%, var(--brand-red) 100%);
  }
  .back-decor {
    position: absolute; inset: 0;
    background: linear-gradient(135deg, rgba(255,255,255,0) 30%, rgba(255,255,255,0.08) 55%, rgba(255,255,255,0) 80%);
  }
  .back-brand {
    position: absolute;
    left: 22px; top: 88px;
    display: flex; align-items: center; gap: 10px;
  }
  .brand-square {
    width: 22px; height: 22px;
    background: var(--brand-red);
  }
  .back-brand .brand-name {
    font-size: 22px;
    color: var(--white);
  }
  .holder {
    position: absolute;
    left: 300px; width: 260px; top: 34px;
    text-align: center;
  }
  .holder-name {
    font-family: "Roboto Condensed", "Arial Narrow", sans-serif;
    font-weight: 700;
    font-size: 20px;
    letter-spacing: 1px;
    color: var(--name-ink);
    text-transform: uppercase;
  }
  .holder-title {
    margin-top: 6px;
    font-size: 16px;
    color: var(--white);
  }
  .contacts {
    position: absolute;
    left: 267px; top: 205px;
    list-style: none;
  }
  .contact {
    display: flex; align-items: center;
    height: 30px;
    margin-bottom: 17px;
    font-size: 17px;
    color: var(--white);
  }
  .contact-icon {
    width: 30px; height: 30px;
    margin-right: 23px;
    flex: none;
  }
</style>
</head>
<body>

<section class="card card-front" aria-label="Card front">
  <div class="front-texture" role="img" aria-label="Subtle repeating brand pattern on dark background"></div>
  <div class="front-brand">
    <p class="brand-name">Keelridge Ventures</p>
    <p class="abn">A.B.N. 71482903165</p>
  </div>
</section>

<section class="card card-back" aria-label="Card back">
  <div class="back-decor" role="img" aria-label="Large faint brand shape decoration"></div>

  <div class="back-brand">
    <span class="brand-square"></span>
    <span class="brand-name">Keelridge Ventures</span>
  </div>

  <div class="holder">
    <p class="holder-name">Daniel Ostrava</p>
    <p class="holder-title">Principal Consultant</p>
  </div>

  <ul class="contacts">
    <li class="contact">
      <svg class="contact-icon" viewBox="0 0 30 30" aria-hidden="true">
        <circle cx="15" cy="15" r="14" fill="#8e2a2f" stroke="var(--icon-ring)" stroke-width="1.5"/>
        <path d="M10.5 8.5l2.5-.5 1.5 3.5-1.8 1.2c.8 1.8 2 3 3.8 3.8l1.2-1.8 3.5 1.5-.5 2.5c-5.5.5-10.7-4.7-10.2-10.2z" fill="#2a1a1b"/>
      </svg>
      <span>+61 452 160 389</span>
    </li>
    <li class="contact">
      <svg class="contact-icon" viewBox="0 0 30 30" aria-hidden="true">
        <circle cx="15" cy="15" r="14" fill="#8e2a2f" stroke="var(--icon-ring)" stroke-width="1.5"/>
        <rect x="9" y="10.5" width="12" height="9" fill="#2a1a1b"/>
        <path d="M9 10.5l6 5 6-5" fill="none" stroke="#8e2a2f" stroke-width="1.2"/>
      </svg>
      <span>daniel@keelridgeventuresconsulting.com.au</span>
    </li>
    <li class="contact">
      <svg class="contact-icon" viewBox="0 0 30 30" aria-hidden="true">
        <circle cx="15" cy="15" r="14" fill="#8e2a2f" stroke="var(--icon-ring)" stroke-width="1.5"/>
        <g fill="none" stroke="#2a1a1b" stroke-width="1.2">
          <circle cx="15" cy="15" r="6.5"/>
          <ellipse cx="15" cy="15" rx="3" ry="6.5"/>
          <path d="M8.5 15h13M9.5 11.5h11M9.5 18.5h11"/>
        </g>
      </svg>
      <span>Web www.keelridgeventuresconsulting.com</span>
    </li>
  </ul>
</section>

</body>
</html>
```